The graphic design project is to create a book cover and potentially an accompanying logo for a book called The Steady Compass: A Field Guide for Guiding Teams Through Shifting Ground. The title is a working title and may change slightly. The book presents 10 capabilities that organizational leaders should have to be able to lead in a world filled with uncertainties. The main themes are the following:• Leaders need to be clear and focused about the overall mission, but also need to make strategic decisions with a diversity of opinions and options.• Leaders must anticipate where they will need to adapt in implementing strategy.• Leaders need to create a culture that promotes trust and agility.• Leaders need to be vigilant and look for early indicators of change. Show intellectual curiosity.• Leaders should be willing to experiment and learn from the experiments.The book is designed as a handbook. This will be a self published business book.The below graphic provides what are the key concepts representing each letter of “STEADY”. The right-hand column provides key words / phrases associated with the concepts.

Target Market(s)

Mid to Senior level executives at global companies across industries.

Colors

Designer to choose colors to be used in the design.

Requirements
Must have
• No must haves.
Nice to have
• Wide open on the design.

```html
<!DOCTYPE html>
<html lang="en">
<head>
<meta charset="utf-8">
<title>The Steady Compass – Book Cover</title>
<link href="https://fonts.googleapis.com/css2?family=EB+Garamond:ital,wght@0,400;0,600;1,400&display=swap" rel="stylesheet">
<style>
  :root {
    --backdrop: #e8e4df;
    --paper: #ffffff;
    --ink: #111111;
    --crimson: #b2393a;
  }
  * { margin: 0; padding: 0; box-sizing: border-box; }
  html, body {
    width: 1200px;
    height: 1200px;
    overflow: hidden;
    background: var(--backdrop);
  }
  .cover {
    position: absolute;
    left: 232px;
    top: 45px;
    width: 736px;
    height: 1107px;
    background: var(--paper);
    font-family: "EB Garamond", Georgia, serif;
    color: var(--ink);
    text-align: center;
  }
  .line {
    position: absolute;
    left: 0;
    width: 100%;
    line-height: 1;
    font-weight: 400;
    white-space: nowrap;
  }
  .series {
    top: 60px;
    font-size: 14px;
    letter-spacing: 0.22em;
    text-transform: uppercase;
  }
  .title-article {
    top: 136px;
    font-size: 34px;
    letter-spacing: 0.22em;
    color: var(--crimson);
  }
  .title-main {
    top: 195px;
    font-size: 80px;
    letter-spacing: 0.08em;
  }
  .title-noun {
    top: 276px;
    font-size: 80px;
    letter-spacing: 0.1em;
    color: var(--crimson);
  }
  .cover-art {
    position: absolute;
    left: 161px;
    top: 458px;
    width: 418px;
    height: 121px;
    background: linear-gradient(90deg,
      rgba(236, 90, 63, 0.0) 0%,
      rgba(236, 90, 63, 0.55) 8%,
      rgba(236, 90, 63, 0.55) 44%,
      rgba(255, 255, 255, 0) 56%,
      rgba(255, 255, 255, 0) 82%,
      rgba(110, 26, 31, 0.55) 88%,
      rgba(110, 26, 31, 0.55) 100%);
    filter: blur(2px);
  }
  .author {
    top: 658px;
    font-size: 64px;
    letter-spacing: 0.14em;
  }
  .author-last { top: 727px; }
  .subtitle {
    top: 836px;
    font-size: 26px;
    font-weight: 600;
    letter-spacing: 0.12em;
    font-variant: small-caps;
    color: var(--crimson);
    line-height: 1.25;
    white-space: normal;
  }
  .epigraph {
    position: absolute;
    left: 88px;
    top: 920px;
    width: 560px;
    font-size: 19px;
    font-style: italic;
    line-height: 1.4;
    letter-spacing: 0.06em;
  }
</style>
</head>
<body>
  <main class="cover">
    <p class="line series">Name of the Series</p>
    <p class="line title-article">THE</p>
    <h1 class="line title-main">STEADY</h1>
    <p class="line title-noun">COMPASS</p>

    <div class="cover-art" role="img" aria-label="Photograph of a group of red game pawns standing apart from a single dark red pawn"></div>

    <p class="line author">AUTHOR</p>
    <p class="line author author-last">LASTNAME</p>

    <h2 class="line subtitle">A Field Guide for Guiding Teams<br>Through Shifting Ground</h2>

    <blockquote class="epigraph">“Leaders need to be clear and focused about the overall mission, but also need to make strategic decisions with a diversity of opinions and options. Leaders must anticipate where they will need to adapt in implementing strategy”</blockquote>
  </main>
</body>
</html>
```